FRESH WEB DESIGN FOR A HEALTH - SOCIAL NETWORK

We are currently looking for a creative, fresh, vibrant, inspiring design for a new social network focused on health and nutrition for health professionals (namely nutritionists) and end-users.

Design requirements - IMPORTANT: please see attached file 'LumaGrove web site design scope' for the detailed brief.

The web site requires new design templates with inter-changeable banners and in some cases profile images. It's important for the website to communicate LumaGrove's core values and image which includes fun, vitality, freshness, life fulfillment, trust, integrity and loyalty to the two target groups. Imagery must have a consistent/inter-related theme across all communities, topics and resources, which need to be easily applied to the web site.To help engage our audience we are looking for something fresh and unique in the selected imagery/ theme/ design templates.

The chosen design will need to be applied to create a PDF, PowerPoint and business card template.

Please see attached file 'LumaGrove web site design scope' to view the LumaGrove web site, which is currently under development.

Industry/Entity Type

Nutrition

```html
<!DOCTYPE html>
<html lang="en">
<head>
<meta charset="utf-8">
<title>LumaGrove – Share your story</title>
<link href="https://fonts.googleapis.com/css2?family=Exo+2:wght@400;600;700;800&family=Noto+Sans:wght@400&display=swap" rel="stylesheet">
<style>
  :root {
    --page-top: #f3f3f3;
    --page-bottom: #fbfbfb;
    --hero-lavender: #b4b6dd;
    --hero-light: #c9cbe8;
    --hero-deep: #a2a2d2;
    --headline-purple: #6a2c8c;
    --nav-bg: rgba(78, 74, 80, 0.86);
    --nav-active: rgba(60, 56, 60, 0.9);
    --nav-divider: rgba(255, 255, 255, 0.14);
    --nav-text: #ffffff;
    --nav-active-text: #f2a51f;
    --login-green: #b3c90d;
    --signup-blue: #0b85c6;
    --welcome-green: #bccf00;
    --body-text: #444444;
    --footer-text: #8a8a8a;
    --icon-grey: #8e8e8e;
    --card-border: #d6d6d6;
    --white: #ffffff;
  }
  * { margin: 0; padding: 0; box-sizing: border-box; }
  html, body { width: 1200px; height: 1003px; overflow: hidden; }
  body {
    background: linear-gradient(to bottom, var(--page-top), var(--page-bottom));
    font-family: "Noto Sans", Verdana, sans-serif;
    position: relative;
  }
  .site { position: absolute; left: 150px; top: 0; width: 900px; }

  .hero {
    position: relative; height: 516px; overflow: hidden;
    background: linear-gradient(120deg, var(--hero-deep) 0%, var(--hero-lavender) 40%, var(--hero-light) 75%, var(--hero-lavender) 100%);
  }
  .hero-photo {
    position: absolute; left: 330px; top: 0; width: 570px; height: 516px;
    background:
      radial-gradient(ellipse 36% 46% at 50% 40%, rgba(232, 196, 168, 0.9) 0%, rgba(222, 184, 150, 0.55) 55%, rgba(200, 190, 220, 0) 100%),
      radial-gradient(ellipse 60% 20% at 50% 100%, rgba(60, 160, 110, 0.55) 0%, rgba(60, 160, 110, 0) 100%);
  }
  .brand {
    position: absolute; left: 19px; top: 18px;
    display: flex; align-items: center; gap: 8px;
    font-family: "Exo 2", sans-serif; font-weight: 600; font-size: 31px; color: var(--white);
  }
  .brand-dot { width: 32px; height: 32px; border-radius: 50%; background: var(--white); }
  .headline {
    position: absolute; left: 84px; top: 210px;
    font-family: "Exo 2", sans-serif; color: var(--headline-purple);
  }
  .headline .lead { display: block; font-size: 34px; font-weight: 400; line-height: 1.1; }
  .headline .strong { display: block; font-size: 46px; font-weight: 800; line-height: 1.2; letter-spacing: -0.5px; }

  .main-nav {
    position: absolute; left: 0; bottom: 0; width: 900px; height: 47px;
    background: var(--nav-bg); display: flex;
    font-family: "Exo 2", sans-serif; font-weight: 600; font-size: 11.5px; text-transform: uppercase;
  }
  .main-nav a {
    display: flex; align-items: center; justify-content: center;
    color: var(--nav-text); text-decoration: none; height: 100%;
    border-right: 1px solid var(--nav-divider);
  }
  .main-nav a.active { color: var(--nav-active-text); background: var(--nav-active); }
  .main-nav .spacer { flex: 1; }
  .main-nav a.login { background: var(--login-green); border: 0; }
  .main-nav a.signup { background: var(--signup-blue); border: 0; }

  .content {
    position: relative; height: 418px; background: var(--white);
    box-shadow: 0 1px 3px rgba(0,0,0,0.08);
  }
  .content h1 {
    position: absolute; left: 38px; top: 44px;
    font-family: "Exo 2", sans-serif; font-weight: 600; font-size: 24.5px; color: var(--welcome-green);
  }
  .intro {
    position: absolute; left: 37px; top: 82px; width: 472px;
    font-size: 12.6px; line-height: 20.6px; color: var(--body-text);
  }
  .intro p + p { margin-top: 20.6px; }
  .video-card {
    position: absolute; left: 525px; top: 86px; width: 338px; height: 234px;
    border: 1px solid var(--card-border); background: var(--white); padding: 4px;
    box-shadow: 0 2px 4px rgba(0,0,0,0.1);
  }
  .video-still {
    position: relative; width: 100%; height: 100%;
    background: linear-gradient(to bottom, #b7d3ea 0%, #d9e6f0 32%, #5c7a4e 48%, #8fb04f 70%, #b3aa93 100%);
  }
  .play-button { position: absolute; left: 50%; top: 50%; transform: translate(-50%, -50%); }

  .site-footer {
    position: absolute; left: 0; top: 958px; width: 900px;
    display: flex; justify-content: space-between; align-items: center;
    font-family: "Exo 2", sans-serif; font-size: 11.8px; color: var(--footer-text);
  }
  .site-footer a { color: var(--footer-text); text-decoration: none; }
  .social { display: flex; gap: 3px; }
  .social span { width: 19px; height: 19px; border-radius: 50%; background: var(--icon-grey); }
</style>
</head>
<body>
  <div class="site">
    <header class="hero">
      <div class="hero-photo" role="img" aria-label="Portrait of a smiling young woman in a green sports top against a lavender backdrop"></div>
      <div class="brand"><span class="brand-dot"></span>LumaGrove</div>
      <h2 class="headline">
        <span class="lead">Share your story &amp;</span>
        <span class="strong">Support Others!</span>
      </h2>
      <nav class="main-nav">
        <a class="active" href="#" style="width:67px">Home</a>
        <a href="#" style="width:76px">Topics</a>
        <a href="#" style="width:112px">Communities</a>
        <a href="#" style="width:67px">Shop</a>
        <a href="#" style="width:61px">FAQ</a>
        <span class="spacer"></span>
        <a class="login" href="#" style="width:67px">Login</a>
        <a class="signup" href="#" style="width:78px">Sign Up</a>
      </nav>
    </header>

    <main class="content">
      <h1>Welcome to LumaGrove</h1>
      <div class="intro">
        <p>LumaGrove’s mission is to help, educate, and inspire people to achieve optimal health and live fulfilled lives. LumaGrove encourages its members, both users and experts, to share their experiences so that people can receive the knowledge, support and inspiration to transform their lives!</p>
        <p>Lorem ipsum dolor sit amet, consectetur adipiscing elit. Duis sed dui ipsum. Proin id nibh eleifend, suscipit nisi congue, molestie enim. In id risus magna. Etiam aliquet massa commodo, sagittis nisi in, efficitur nulla. Mauris tristique mauris id placerat cursus. Morbi feugiat, tellus at cursus dignissim, libero felis fermentum urna, vitae fermentum urna arcu at enim. Mauris iaculis urna sit amet nibh lacinia, non ornare massa luctus. Ut vestibulum mauris nec tellus ornare finibus. Suspendisse semper erat elit.</p>
      </div>
      <div class="video-card">
        <div class="video-still" role="img" aria-label="Video still: a group of friends jogging along a country path on a sunny day">
          <svg class="play-button" width="72" height="72" viewBox="0 0 72 72" aria-hidden="true">
            <circle cx="36" cy="36" r="32" fill="rgba(255,255,255,0.15)" stroke="#ffffff" stroke-width="5"/>
            <path d="M29 22 L52 36 L29 50 Z" fill="#ffffff"/>
          </svg>
        </div>
      </div>
    </main>

    <footer class="site-footer">
      <div>©2014 LumaGrove. &nbsp;|&nbsp; <a href="#">Privacy Policy</a></div>
      <div class="social" aria-label="Social links">
        <span></span><span></span><span></span><span></span><span></span>
      </div>
    </footer>
  </div>
</body>
</html>
```